Urkundendesign für Jahrgangsbeste einer Realschule gesucht
Zielgruppe
Der Elternbeirat der Realschule Felkenried benötigt für die Jahrgangsbesten des Abschlussjahrgangs eine Urkunde. Gerne mit Prägung (was kostet sowas bei Druck?!?). Das von-Haltmoor-Logo darf benutzt werden (siehe Homepage).
es soll eine Urkunde für den/die 'Jahrgangsbeste 2026' geben. das Datum, sowie SchülerInnen-Name würden wir jeweils handschriftlich anbringen.
die Urkunde in A4 gestalten.
wir benötigen die üblichen druckbaren Dateien, sodass eine Druckerei dann auch selbst Jahr für Jahr das Jahr abändern kann.
Aufgabenstellung
bitte um Vorschläge, wir arbeiten uns nach und nach da durch.
nicht zu viel Schnörkelei.

```html
<!DOCTYPE html>
<html lang="de">
<head>
<meta charset="utf-8">
<title>Urkunde Jahrgangsbeste 2026</title>
<link rel="stylesheet" href="https://fonts.googleapis.com/css2?family=Cinzel:wght@400;700&family=Playfair+Display:wght@800&family=Pinyon+Script&family=Figtree:wght@400;600&display=swap">
<style>
  :root {
    --paper: #f4f4f3;
    --green: #4caf3f;
    --green-light: #66c25a;
    --teal: #1aa595;
    --teal-light: #55c9bc;
    --yellow: #f6c31a;
    --ink: #1b1b1b;
  }
  * { margin: 0; padding: 0; box-sizing: border-box; }
  html, body { width: 727px; height: 1200px; overflow: hidden; background: var(--paper); }
  .certificate { position: relative; width: 727px; height: 1200px; background: var(--paper); overflow: hidden; }
  .border-band { position: absolute; left: 0; width: 727px; height: 110px; }
  .border-band.top {
    top: 0;
    background: linear-gradient(180deg, var(--green-light) 0%, var(--yellow) 70%, rgba(244,244,243,0) 100%);
  }
  .border-band.bottom {
    bottom: 0;
    background: linear-gradient(0deg, var(--green-light) 0%, var(--yellow) 70%, rgba(244,244,243,0) 100%);
  }
  .content { position: absolute; inset: 0; text-align: center; }
  .issuer {
    position: absolute; top: 222px; left: 0; right: 0;
    display: flex; align-items: center; justify-content: center; gap: 12px;
    font-family: "Figtree", sans-serif; font-weight: 600; font-size: 30px; color: var(--teal);
  }
  .issuer-dot { width: 22px; height: 22px; border-radius: 50%; background: var(--teal); }
  .eyebrow {
    position: absolute; top: 356px; left: 0; right: 0;
    font-family: "Cinzel", serif; font-size: 25px; color: var(--green); letter-spacing: 0.5px;
  }
  .title {
    position: absolute; top: 390px; left: 0; right: 0;
    font-family: "Playfair Display", serif; font-weight: 800; font-size: 58px; line-height: 62px;
    color: var(--teal); letter-spacing: -0.5px;
    font-variant-numeric: lining-nums;
  }
  .dedication {
    position: absolute; top: 538px; left: 0; right: 0;
    font-family: "Cinzel", serif; font-weight: 700; font-size: 15px; color: var(--ink);
  }
  .recipient {
    position: absolute; top: 592px; left: 0; right: 0;
    font-family: "Pinyon Script", cursive; font-size: 66px; line-height: 80px; color: var(--green);
  }
  .recipient-line { position: absolute; top: 681px; left: 103px; width: 520px; height: 1.5px; background: var(--teal); }
  .body-text {
    position: absolute; top: 745px; left: 0; right: 0;
    font-family: "Figtree", sans-serif; font-size: 15px; line-height: 21px; color: var(--ink);
  }
  .sign-field { position: absolute; top: 936px; width: 236px; border-top: 1.3px solid var(--ink); padding-top: 8px;
    font-family: "Figtree", sans-serif; font-weight: 600; font-size: 16px; color: var(--ink); }
  .sign-field.signature { left: 111px; }
  .sign-field.date { left: 380px; }
</style>
</head>
<body>
<main class="certificate">
  <div class="border-band top" role="img" aria-label="Dekorative Bordüre in Grün, Gelb und Türkis am oberen Rand"></div>
  <div class="border-band bottom" role="img" aria-label="Dekorative Bordüre in Grün, Gelb und Türkis am unteren Rand"></div>

  <section class="content">
    <div class="issuer"><span class="issuer-dot"></span>von-Haltmoor</div>
    <p class="eyebrow">URKUNDE FÜR DEN/DIE</p>
    <h1 class="title">JAHRGANGSBESTE<br>2026</h1>
    <p class="dedication">DIESES ZERTIFIKAT WIRD MIT STOLZ ÜBERREICHT AN</p>
    <p class="recipient">Lorem Ipsum</p>
    <div class="recipient-line"></div>
    <p class="body-text">Lorem ipsum dolor sit amet, consectetur adipiscing elit, sed do<br>eiusmod tempor incididunt ut labore et dolore magna aliqua.<br>Ut enim ad minim veniam, quis nostrud exercitation ullamco<br>laboris nisi ut aliquip ex ea commodo consequat.</p>
    <div class="sign-field signature">Unterschrift</div>
    <div class="sign-field date">Datum</div>
  </section>
</main>
</body>
</html>
```